Blue Heron Courier & Delivery Services needs a flyer

We need an introductory flyer for a new company based in Yellowknife, Northwest Territories,Canada. Our company name is Blue Heron Courier & Delivery Services. We will be handling envelopes and small packages up to 20 pounds. We expect 20 percent of our business to come from residential customers and 80 percent from the business community including lawyers, doctors, engineers and government offices. The main message that we will try to convey in this flyer is that we are a new and exciting company that promises to make 100% customer satisfaction our number one goal. I would like the layout to be elegant and simple and certainly not cluttered. It will be a single sided flyer. Text should be easy to read and most likely at most two fonts. I would like one stunning image or photo relating to the courier business and message. There should be plenty of white space throughout the flyer and nice margins on all sides. I would like my flyer to be 8.5 inches by 11 inches and it should read from top to bottom. . I would like a nice big bold headline that in some way mentions " Special Offer- Up to 100% Off. You can change the wording if you have a better idea. Throughout the flyer you can highlight and italicize for emphasis. Please try to use bullet points for my five main reasons for hiring our company which are: you will be 100% satisfied with each delivery or you will be given a complete refund no questions asked, your envelope or package will be delivered on time every time, you will always be treated throughout the delivery process in a professional manner, you will be given the widest selection in Yellowknife of price points and delivery options , you can trust us with your most important and time sensitive deliveries. Try to incorporate something next to these five points to really draw attention like a check mark, star etc.... I would prefer if my company name and contact info is in the bottom third of the flyer. My email is blueheroncourieryk@mailbox-example.net. My phone number is 867-312-7794. It might be a good idea to have my phone number also at the top of the flyer someplace after the headline saying like Call Now!!! you can use boxes, borders and contrasting bold colors to bring flyer to life. I have a testimonial from a business owner that I dealt with when I ran another business which would be nice to have included . " While receiving daily deliveries for 18 years from Calvin Marsh I found him to be punctual , reliable and efficient " Glen Potter, owner of Potter and Lindqvist Trading LTD, Yellowknife,NWT. I thought perhaps at the top of flyer after the headline perhaps in some way you could say Yellowknife's newest and best courier and delivery service is pleased to offer the following stunning discounts: then you could list the three special offers: 1) First 5 businesses to book regular scheduled deliveries will get 100% off their first delivery. 2) First 5 businesses to book a single delivery will get 50% off that delivery. 3) First 5 residential customers to book a delivery will receive 25% off that delivery. I thought you could mention my name somewhere. Calvin Marsh. Owner has lived in Yellowknife for 42 years and has 20 years experience doing performing important and time sensitive deliveries. Perhaps you could mention somewhere that we will have a couple of ongoing discounts also which will be 1) seniors discounts. 2) regular scheduled deliveries discounts. I have suggested colors but if you have other ideas I would certainly look at them. Our business tag line is. On Time Every Time
Target Market(s)
Business owners typically males 30-50 years old
Industry/Entity Type
Delivery Service
Requirements
Must have
- Done in CMYK mode sufficient bleed size for printing
Nice to have
- Nothing set in stone. I recently had my logo design uploaded to this brief. It is up to you if you feel it should be included in the flyer.
Should not have
- I am willing to look at any design

```html
<!DOCTYPE html>
<html lang="en">
<head>
<meta charset="utf-8">
<title>Blue Heron Courier &amp; Delivery Services — Flyer</title>
<link rel="stylesheet" href="https://fonts.googleapis.com/css2?family=Source+Sans+3:ital,wght@0,400;0,600;0,700;1,400;1,600;1,700&display=swap">
<style>
  :root {
    --brand-blue: #4a55a8;
    --rule-purple: #5a5fb4;
    --grey-text: #5a5a5a;
    --teal-top: #139fc6;
    --teal-mid: #1fb1d2;
    --teal-bottom: #35c4dc;
    --white: #ffffff;
    --check: #6a6fd2;
    --quote-yellow: #f6ec8c;
    --footer-cream: #f8f4c6;
    --footer-text: #3a3a3a;
    --photo-light: #e9e4dc;
    --photo-dark: #b98f62;
  }
  * { margin: 0; padding: 0; box-sizing: border-box; }
  html, body { width: 927px; height: 1200px; overflow: hidden; background: var(--white); }
  .flyer {
    position: relative;
    width: 927px;
    height: 1200px;
    font-family: "Source Sans 3", Arial, sans-serif;
    background: var(--white);
    overflow: hidden;
  }
  .header { position: absolute; left: 0; top: 0; width: 927px; height: 247px; background: var(--white); }
  .headline {
    position: absolute; left: 45px; top: 14px;
    color: var(--brand-blue);
    font-weight: 700; font-size: 66px; line-height: 66px;
    letter-spacing: 0.3px;
  }
  .call-now {
    position: absolute; left: 47px; top: 176px;
    color: var(--grey-text); font-size: 30px; font-weight: 400;
  }
  .call-now .number { font-size: 36px; }
  .hero-photo {
    position: absolute; right: 0; top: 0; width: 215px; height: 243px;
    background: radial-gradient(ellipse at 45% 40%, var(--photo-light) 0%, #d6c2a6 55%, var(--photo-dark) 100%);
  }
  .header-rule { position: absolute; left: 0; top: 243px; width: 927px; height: 6px; background: var(--rule-purple); }

  .offers {
    position: absolute; left: 0; top: 249px; width: 927px; height: 819px;
    background: linear-gradient(165deg, var(--teal-top) 0%, var(--teal-mid) 45%, var(--teal-bottom) 100%);
    color: var(--white);
  }
  .intro {
    position: absolute; left: 45px; top: 22px; width: 850px;
    font-style: italic; font-weight: 700; font-size: 26px; line-height: 37px;
  }
  .benefits { position: absolute; left: 179px; top: 108px; width: 640px; list-style: none; }
  .benefits li {
    position: relative; padding-left: 33px; margin-bottom: 2px;
    font-style: italic; font-size: 21.5px; line-height: 31px;
  }
  .benefits li svg { position: absolute; left: 0; top: 7px; width: 20px; height: 20px; }

  .divider { position: absolute; left: 45px; top: 690px; width: 841px; height: 16px; }

  .testimonial {
    position: absolute; left: 58px; top: 712px; width: 840px;
    color: var(--quote-yellow); font-style: italic; font-weight: 700;
    font-size: 22.5px; line-height: 30px;
  }
  .testimonial .second-line { padding-left: 26px; }
  .attribution { position: absolute; right: 44px; top: 744px; text-align: right; color: var(--white); }
  .attribution .name { color: var(--quote-yellow); font-weight: 700; font-size: 19px; line-height: 22px; }
  .attribution .company { font-size: 14px; line-height: 18px; font-weight: 600; }

  .footer {
    position: absolute; left: 0; top: 1068px; width: 927px; height: 132px;
    background: var(--footer-cream); color: var(--footer-text);
  }
  .owner-bio {
    position: absolute; left: 35px; top: 13px; width: 480px;
    font-size: 18px; line-height: 27px; font-style: italic;
  }
  .owner-bio .owner-name { font-style: normal; font-weight: 600; }
  .contact { position: absolute; left: 530px; top: 30px; list-style: none; }
  .contact li { display: flex; align-items: center; font-size: 21px; line-height: 28px; margin-bottom: 15px; }
  .contact svg { width: 26px; height: 22px; margin-right: 14px; }
</style>
</head>
<body>
<div class="flyer">
  <header class="header">
    <h1 class="headline">Blue Heron Courier<br>&amp; Delivery Services</h1>
    <p class="call-now">Call now: <span class="number">867-312-7794</span></p>
    <div class="hero-photo" role="img" aria-label="Smiling courier carrying a stack of cardboard parcels"></div>
    <div class="header-rule"></div>
  </header>

  <section class="offers">
    <p class="intro">Yellowknife’s newest and best courier and delivery service is pleased to offer the following stunning discounts</p>
    <ul class="benefits">
      <li><svg viewBox="0 0 20 20"><rect x="1.5" y="3.5" width="14" height="14" fill="none" stroke="var(--check)" stroke-width="2"/><path d="M4.5 10 L8.5 14 L18.5 2.5" fill="none" stroke="var(--check)" stroke-width="2.6"/></svg>100% satisfaction with each delivery or you will be given acomplete refund noquestions asked,</li>
      <li><svg viewBox="0 0 20 20"><rect x="1.5" y="3.5" width="14" height="14" fill="none" stroke="var(--check)" stroke-width="2"/><path d="M4.5 10 L8.5 14 L18.5 2.5" fill="none" stroke="var(--check)" stroke-width="2.6"/></svg>On time delivery! Every time.</li>
      <li><svg viewBox="0 0 20 20"><rect x="1.5" y="3.5" width="14" height="14" fill="none" stroke="var(--check)" stroke-width="2"/><path d="M4.5 10 L8.5 14 L18.5 2.5" fill="none" stroke="var(--check)" stroke-width="2.6"/></svg>You will always be treated throughout the delivery process in a professional manner,</li>
      <li><svg viewBox="0 0 20 20"><rect x="1.5" y="3.5" width="14" height="14" fill="none" stroke="var(--check)" stroke-width="2"/><path d="M4.5 10 L8.5 14 L18.5 2.5" fill="none" stroke="var(--check)" stroke-width="2.6"/></svg>You will be given the widest selection in Yellowknife of price points and delivery options ,</li>
      <li><svg viewBox="0 0 20 20"><rect x="1.5" y="3.5" width="14" height="14" fill="none" stroke="var(--check)" stroke-width="2"/><path d="M4.5 10 L8.5 14 L18.5 2.5" fill="none" stroke="var(--check)" stroke-width="2.6"/></svg>You can trust us with your most important and time sensitive deliveries.</li>
      <li><svg viewBox="0 0 20 20"><rect x="1.5" y="3.5" width="14" height="14" fill="none" stroke="var(--check)" stroke-width="2"/><path d="M4.5 10 L8.5 14 L18.5 2.5" fill="none" stroke="var(--check)" stroke-width="2.6"/></svg>Seniors discounts.</li>
      <li><svg viewBox="0 0 20 20"><rect x="1.5" y="3.5" width="14" height="14" fill="none" stroke="var(--check)" stroke-width="2"/><path d="M4.5 10 L8.5 14 L18.5 2.5" fill="none" stroke="var(--check)" stroke-width="2.6"/></svg>Regular scheduled deliveries discounts.</li>
      <li><svg viewBox="0 0 20 20"><rect x="1.5" y="3.5" width="14" height="14" fill="none" stroke="var(--check)" stroke-width="2"/><path d="M4.5 10 L8.5 14 L18.5 2.5" fill="none" stroke="var(--check)" stroke-width="2.6"/></svg>First 5 businesses to book regular scheduled deliveries will get 100% off their first delivery.</li>
      <li><svg viewBox="0 0 20 20"><rect x="1.5" y="3.5" width="14" height="14" fill="none" stroke="var(--check)" stroke-width="2"/><path d="M4.5 10 L8.5 14 L18.5 2.5" fill="none" stroke="var(--check)" stroke-width="2.6"/></svg>First 5 businesses to book a single delivery will get 50% off that delivery.</li>
      <li><svg viewBox="0 0 20 20"><rect x="1.5" y="3.5" width="14" height="14" fill="none" stroke="var(--check)" stroke-width="2"/><path d="M4.5 10 L8.5 14 L18.5 2.5" fill="none" stroke="var(--check)" stroke-width="2.6"/></svg>First 5 residential customers to book a delivery will receive 25% off that delivery.</li>
    </ul>

    <svg class="divider" viewBox="0 0 841 16" aria-hidden="true">
      <line x1="0" y1="8" x2="841" y2="8" stroke="var(--quote-yellow)" stroke-width="2"/>
      <circle cx="418" cy="8" r="7.5" fill="var(--quote-yellow)"/>
    </svg>

    <blockquote class="testimonial">
      <p>“ While receiving daily deliveries for 18 years from Calvin Marsh I found him</p>
      <p class="second-line">to be punctual , reliable and efficient ”</p>
    </blockquote>
    <div class="attribution">
      <p class="name">Glen Potter</p>
      <p class="company">Potter and Lindqvist Trading LTD,</p>
      <p class="company">Yellowknife, NWT</p>
    </div>
  </section>

  <footer class="footer">
    <p class="owner-bio"><span class="owner-name">Calvin Marsh.</span> Owner has lived in Yellowknife for 42 years and has 20 years experience doing performing important and time sensitive deliveries.</p>
    <ul class="contact">
      <li><svg viewBox="0 0 26 22" aria-hidden="true"><path d="M3 6 L23 2 L20 19 L12 14 L8 18 L8 12 Z" fill="none" stroke="var(--footer-text)" stroke-width="1.8" stroke-linejoin="round"/><path d="M8 12 L23 2" stroke="var(--footer-text)" stroke-width="1.8"/></svg>blueheroncourieryk@mailbox-example.net</li>
      <li><svg viewBox="0 0 26 22" aria-hidden="true"><path d="M2 8 Q13 1 24 8 L22 11 L18 10 L17 7 Q13 6 9 7 L8 10 L4 11 Z" fill="var(--footer-text)"/><path d="M6 12 L20 12 L22 20 L4 20 Z" fill="var(--footer-text)"/></svg>867-312-7794</li>
    </ul>
  </footer>
</div>
</body>
</html>
```